PLOVEN Business Card

Coastal Build Additions and Refits. I need a business card designed for this new high end renovation business. I would like the logo centered on the back side with the ABN (37 915 402 176) on the bottom right hand corner.

I would like the following information placed on the other side along with some customized pattern or design.

Derek Collwood
Director
Phone: 1300 480 957
Fax: (02) 8145 9021
Website: www.plovenbuilders.com.au
Email: d.collwood@plovenbuilders.com.au
PO Box 87,
Kelvinbrook NSW 2069

(FB Logo) PLOVEN - Coastal Build Additions and Refits

The final design should communicate professionalism and trust.

Back side background colour: white
Front side: Undecided

```html
<!DOCTYPE html>
<html lang="en">
<head>
<meta charset="utf-8">
<title>PLOVEN Business Card</title>
<link href="https://fonts.googleapis.com/css2?family=Source+Sans+3:ital,wght@0,400;0,600;0,700;1,400&display=swap" rel="stylesheet">
<style>
  :root {
    --navy: #1c4f8c;
    --ink: #1e1e1e;
    --muted: #3a4452;
    --edge: #a9a9a9;
    --paper: #ffffff;
  }
  * { box-sizing: border-box; margin: 0; padding: 0; }
  html, body {
    width: 1012px; height: 1200px; overflow: hidden;
    background: var(--paper);
    font-family: "Source Sans 3", "Myriad Pro", Arial, sans-serif;
    color: var(--ink);
  }
  .card {
    position: absolute; left: 130px; width: 736px;
    background: var(--paper);
    border: 1.5px solid var(--edge);
    overflow: hidden;
  }
  .card-front { top: 168px; height: 424px; }
  .card-back { top: 636px; height: 420px; }

  .holder-name {
    position: absolute; left: 28px; top: 20px;
    font-size: 27px; font-weight: 700; letter-spacing: 0.2px;
  }
  .holder-role {
    position: absolute; left: 140px; top: 54px;
    font-size: 25px; font-style: italic;
  }
  .arc-top { position: absolute; left: 0; top: 0; }
  .arc-corner { position: absolute; right: 0; bottom: 0; }

  .contact-list { position: absolute; left: 196px; top: 160px; list-style: none; }
  .contact-item {
    display: flex; align-items: center; height: 34px;
    font-size: 25px;
  }
  .contact-item.gap { margin-top: 34px; }
  .contact-item.web span:last-child { font-style: italic; }
  .key {
    display: inline-flex; align-items: center; justify-content: center;
    width: 29px; height: 30px; margin-right: 23px;
    border: 2px solid var(--ink); border-radius: 7px;
    font-size: 22px; font-weight: 700; line-height: 1;
  }
  .postal {
    position: absolute; left: 248px; top: 360px;
    font-size: 25px;
  }

  .brand {
    position: absolute; left: 0; right: 0; top: 156px;
    text-align: center;
  }
  .brand-name {
    font-size: 60px; font-weight: 700; color: var(--navy);
    letter-spacing: 3px; line-height: 1;
  }
  .brand-tagline {
    display: flex; align-items: center; justify-content: center;
    gap: 8px; margin-top: 12px;
    font-size: 14px; letter-spacing: 1px; color: var(--navy);
    text-transform: uppercase;
  }
  .brand-tagline::before, .brand-tagline::after {
    content: ""; width: 34px; height: 1.5px; background: var(--navy);
  }
  .abn {
    position: absolute; right: 16px; bottom: 12px;
    font-size: 15px;
  }
</style>
</head>
<body>
  <section class="card card-front">
    <svg class="arc-top" width="736" height="424" viewBox="0 0 736 424" aria-hidden="true">
      <path d="M14 158 C150 110 380 110 496 154 C380 124 160 124 14 158 Z" fill="var(--navy)"/>
    </svg>
    <svg class="arc-corner" width="90" height="90" viewBox="0 0 90 90" aria-hidden="true">
      <path d="M28 90 C56 70 68 40 66 22 C82 40 82 70 78 90 Z" fill="var(--navy)"/>
    </svg>

    <h1 class="holder-name">Derek Collwood</h1>
    <p class="holder-role">Director</p>

    <ul class="contact-list">
      <li class="contact-item"><span class="key">P</span><span>1300 480 957</span></li>
      <li class="contact-item"><span class="key">F</span><span>(02) 8145 9021</span></li>
      <li class="contact-item web gap"><span class="key">W</span><span>www.plovenbuilders.com.au</span></li>
      <li class="contact-item"><span class="key">E</span><span>d.collwood@plovenbuilders.com.au</span></li>
    </ul>
    <p class="postal">PO Box 87, Kelvinbrook NSW 2069</p>
  </section>

  <section class="card card-back">
    <div class="brand">
      <div class="brand-name">PLOVEN</div>
      <div class="brand-tagline">Coastal Build Additions &amp; Refits</div>
    </div>
    <p class="abn">ABN (37 915 402 176)</p>
  </section>
</body>
</html>
```